Vereins Website
Zielgruppe
Webiste für den Verein 'Katzenhain Oberlau' (details siehe Anhang).
Ziel der Website:
- Sponsoren finden
- Vereinsmitglieder finden & Interessen bündeln.
Aufgabenstellung
Die Webiste sollt aufgeräumt, übersichtlich und freundlich wirken.

```html
<!DOCTYPE html>
<html lang="de">
<head>
<meta charset="utf-8">
<title>Verein Katzenhain Oberlau</title>
<link href="https://fonts.googleapis.com/css2?family=Arimo:wght@400;700&display=swap" rel="stylesheet">
<style>
:root{
  --orange:#f39200;
  --ink:#1d1d1b;
  --field:#e3e3e3;
  --tile:#dadada;
  --tile-dark:#bcbcbc;
  --band:#e6e6e6;
  --footer:#878787;
  --white:#ffffff;
  --slip:#8a8a8a;
}
*{box-sizing:border-box;margin:0;padding:0}
html,body{width:1200px;height:3344px;overflow:hidden;background:var(--white)}
body{position:relative;font-family:"Arimo",Arial,sans-serif;color:var(--ink)}
.abs{position:absolute}
.center{left:0;width:1200px;text-align:center}

.site-header{left:0;top:0;width:1200px;height:160px;background:var(--orange)}
.brand-kicker{top:66px;font-size:19px;letter-spacing:8px;color:var(--ink)}
.brand-name{top:92px;font-size:42px;font-weight:700;color:var(--white);letter-spacing:1px;text-transform:uppercase}

.hero{left:0;top:160px;width:1200px;height:620px;
  background:linear-gradient(180deg,#c9ccc8 0%,#5d6a4e 22%,#b08a5e 45%,#9a6a3c 70%,#c8a57a 100%)}

.intro-title{top:846px;font-size:35px;font-weight:700;color:var(--orange);letter-spacing:2px;line-height:40px}
.intro-text{top:948px;font-size:11.5px;letter-spacing:2.6px;line-height:18.8px;text-transform:uppercase}
.intro-text b{font-weight:700}

.join-title{top:1138px;font-size:22px;font-weight:700;letter-spacing:1.2px}
.label{font-size:12.5px;letter-spacing:2.6px;text-transform:uppercase}
.field{background:var(--field)}
.button{background:var(--orange);color:var(--white);font-size:10px;letter-spacing:3px;text-align:center;box-shadow:0 3px 4px rgba(0,0,0,.25);text-transform:uppercase}
.join-note{top:1570px;font-size:13px;letter-spacing:.8px;line-height:17px}

.help-title{top:1690px;font-size:46px;font-weight:700;color:var(--orange);letter-spacing:2px}
.help-sub{top:1740px;font-size:26px;letter-spacing:5px}
.dog-visual{left:340px;top:1805px;width:511px;height:203px;border-radius:180px 180px 0 0;
  background:radial-gradient(ellipse at 50% 80%,#c46a1e 0%,#a8541a 45%,#6b3a1c 100%)}
.bank-box{left:90px;top:2008px;width:1018px;height:217px;background:var(--orange);color:var(--white);text-align:center}
.bank-box .title{position:absolute;left:0;right:0;top:43px;font-size:29px;font-weight:700;letter-spacing:1.5px}
.bank-box .line{position:absolute;left:0;right:0;font-size:19px;letter-spacing:1px}

.section-title{font-size:28px;font-weight:700;letter-spacing:2px}
.tile{background:var(--tile)}
.tile-offer{background:var(--tile-dark);color:var(--white);font-size:17px;letter-spacing:1px;line-height:23px;text-align:center;display:flex;align-items:center;justify-content:center}

.pay{display:flex;align-items:center;justify-content:center;background:var(--tile);color:var(--ink);font-size:17px;letter-spacing:1px;font-weight:400;text-transform:uppercase}
.pay-slip{background:none;border:3px solid var(--slip);font-size:16px;color:#555}

.contact{left:0;top:2951px;width:1200px;height:335px;background:var(--band)}
.contact-title{top:3000px;font-size:19px;font-weight:700;letter-spacing:1.6px}
.contact-field{background:var(--white);padding:14px 10px;font-size:12.5px;letter-spacing:2.6px}

.site-footer{left:0;top:3286px;width:1200px;height:58px;background:var(--footer);color:var(--white);font-size:14px;letter-spacing:.8px;display:flex;align-items:center;justify-content:center}
</style>
</head>
<body>

<header class="abs site-header"></header>
<div class="abs center brand-kicker">VEREIN</div>
<div class="abs center brand-name">Katzenhain Oberlau</div>

<div class="abs hero" role="img" aria-label="Foto: Hund wälzt sich auf einer Wiese mit trockenem Gras"></div>

<h1 class="abs center intro-title">EIN BEGEGNUNGSORT FÜR DIE GANZE REGION,<br>VON DEM ALLE PROFITIEREN.</h1>
<p class="abs center intro-text">
Nach dem Vorbild von <b>Moosbach</b> möchten wir in Oberlau eine<br>
eingezäunte Hundespielwiese auf die Beine stellen und damit<br>
das Wohlergehen der Hunde fördern.<br>
Auf der eingezäunten Wiese können die Hunde ohne Leinenzwang spielen, sich<br>
austoben und sozialisieren.<br>
Gleichzeitig schafft dies einen Raum, in dem sich die Hundehalter treffen und<br>
austauschen können.
</p>

<h2 class="abs center join-title">PROJEKT UNTERSTÜTZEN UND VEREINSMITGLIED* WERDEN:</h2>
<div class="abs label" style="left:304px;top:1194px">Vorname</div>
<div class="abs label" style="left:623px;top:1194px">Nachname</div>
<div class="abs field" style="left:295px;top:1218px;width:300px;height:37px"></div>
<div class="abs field" style="left:614px;top:1218px;width:300px;height:37px"></div>
<div class="abs label" style="left:304px;top:1272px">Strasse | Hausnummer</div>
<div class="abs field" style="left:295px;top:1296px;width:619px;height:37px"></div>
<div class="abs label" style="left:304px;top:1350px">PLZ | Ort</div>
<div class="abs field" style="left:295px;top:1374px;width:619px;height:37px"></div>
<div class="abs label" style="left:304px;top:1429px">E-Mail-Adresse</div>
<div class="abs field" style="left:295px;top:1453px;width:619px;height:37px"></div>
<div class="abs button" style="left:499px;top:1510px;width:176px;height:33px;line-height:33px">Absenden</div>
<p class="abs center join-note">EINE VEREINSMITGLIEDSCHAFT IST DERZEIT NOCH KOSTENLOS.<br>SIE UNTERSTÜTZEN DEN VEREIN DAMIT IDEELL.</p>

<h2 class="abs center help-title">HELFEN SIE UNS</h2>
<div class="abs center help-sub">DIESES PROJEKT ZU VERWIRKLICHEN</div>
<div class="abs dog-visual" role="img" aria-label="Foto: Hund schaut über den Rand des Spendenkontos"></div>
<div class="abs bank-box">
  <div class="title">SPENDENKONTO:</div>
  <div class="line" style="top:86px">KATZENHAIN OBERLAU</div>
  <div class="line" style="top:124px">IBAN: 98 00000 00000 00000 9</div>
  <div class="line" style="top:161px">BIC: 6553873</div>
</div>

<h2 class="abs center section-title" style="top:2276px">FÜR SPONSOREN</h2>
<div class="abs tile" style="left:343px;top:2338px;width:121px;height:121px"></div>
<div class="abs tile" style="left:479px;top:2338px;width:121px;height:121px"></div>
<div class="abs tile-offer" style="left:616px;top:2338px;width:259px;height:121px">HIER KÖNNTE<br>IHR LOGO STEHEN</div>
<div class="abs tile" style="left:343px;top:2473px;width:258px;height:121px"></div>
<div class="abs tile" style="left:616px;top:2473px;width:122px;height:121px"></div>
<div class="abs tile" style="left:753px;top:2473px;width:122px;height:121px"></div>

<h2 class="abs center section-title" style="top:2657px">FÜR PRIVTE SPENDEN</h2>
<div class="abs pay" style="left:409px;top:2713px;width:95px;height:95px;font-size:13px">Klickgeld</div>
<div class="abs pay" style="left:547px;top:2713px;width:262px;height:95px">Zahlwerk</div>
<div class="abs pay" style="left:357px;top:2838px;width:227px;height:52px">Geldbote</div>
<div class="abs pay pay-slip" style="left:618px;top:2848px;width:220px;height:38px">EINZAHLUNGSSCHEIN</div>

<section class="abs contact"></section>
<h2 class="abs center contact-title">WIR FREUEN UNS AUF IHRE ANREGUNGEN &amp; IDEEN:</h2>
<div class="abs contact-field" style="left:275px;top:3039px;width:324px;height:39px">NAME</div>
<div class="abs contact-field" style="left:619px;top:3039px;width:325px;height:39px">E-MAIL-ADRESSE</div>
<div class="abs contact-field" style="left:275px;top:3099px;width:669px;height:82px;padding-top:10px">IHRE NACHRICHT</div>
<div class="abs button" style="left:496px;top:3201px;width:191px;height:34px;line-height:34px">Absenden</div>

<footer class="abs site-footer">COPYRIGHT © 2019 | INFO@KATZENHAIN-OBERLAU.CH</footer>

</body>
</html>
```